Paper Lantern Design

Query PixelTent: THE PAPER LANTERN LEDGER
(commercial fiction, 85,000 words)

AUTHOR: Peter L. Hoskins [pen name] Author: Owen Carl Fenwick
Tamsin Ogilvy

Mass shooter, quadroon Ross Pemberley, schools reporter Lorraine Dawkins. Jewish commodity trader, Ari Lefkowitz, schools his trading partner, Neil Foster, on how it feels to be a minority. Pemberley’s shooting lands Ari in a coma, and they all school each other. How did they get so ignorant? And about what? Trading, i.e., capitalism. Politics, i.e., corruption. Killing, i.e., war. The stuff you only say in public, never with a friend of another ethnicity, i.e., racism. Therefore, the topic of this novel is allodoxaphobia. [stay with me]

How many gears does an Italian tank have? It’s got nineteen in reverse and one in forward in case the enemy attacks from the rear. If ethnic comedy is offensive, you might have caught allodoxaphobia.

Allodoxaphobia? A plague spreads unseen through America. It’s faced by a financial wizard [Jew boy], his partner [Whitey], and an African-American news lady. Three subcultures face allodoxaphobia—fear of conflicting opinions.

Lorraine Dawkins is sent with Frank “Mule” Kessler to cover a mass shooting in the Jewish suburb of Highland Park. KQT news gets her to take commodity trader, Neil Foster, to interview the quadroon shooter, Ross Pemberley, who justifies himself with brutal, woke truth that forces Lorraine to drop every racial inhibition and engage the Whitey with a variety of inappropriate interracial topics. Neil’s Jewish trading partner, Ari Lefkowitz, cannot be interviewed due to his coma.

Shooter, Pemberley, opens the door to the issues—war, capitalism, corruption, and race. All the issues climax at Ari’s memorial and Shiva.

Neil and Lorraine eventually turn romantic and the tension of the issues builds. Ross is shown to be a troubled shooter but not the killer. Ari’s brother has the fake art, “Dusk over Carmel,” and the KQT mole, a buxom beauty, uncovers corruption in the Lakeshore Watch.

QUALIFICATION? Fenwick’s childhood gets the blame—the Jim Crow South and the bazaars of Kabul, Afghanistan. Fenwick drove a bus on the Southside of Chicago, listened to innocent criminals for half a decade as a jail guard, then spent his careen trading in the pits of the Harvest Exchange. Hot tip from the floor: THE CROWD IS ALWAYS WRONG. It took Fenwick a couple of years to understand the meme, and a couple decades to resolve the themes of this novel.

WRITINGS His memoir, Ashes on the Ledger, was published by Brightwater, and he wrote Voice of the Mangroves, the memoir of an Amazon shaman. (both have sold about 40,000) He’s a member of Leon Tabbert’s Pit Oracle series.

COMPARABLES: (You’ll know this better than I)
Pelham’s Tobias Reedle for its emotional connections [and maybe racial language]
Voronkin’s Sisters Belovskaya, The spiritual themes are not as overt as Voronkin’s, but the undercurrent is audible for those with “ears to hear.”
Walter Quince's 2061 is more political and graphic. Nevertheless, child rape is graphic
Hartley, “A Harvest Ballad”
Samuel Branford’s, Edge of Silence
Maddox’s, “King of the Gulls,”

Best regards,
Owen Fenwick
https://owenfenwickpages.example/

African American, Jewish, manorities, academics, home schoolers

SIZE -- approx 9 X 6

• you can choose this
• I've sent many pictures and descriptions of the novel
• foul or off color pics

```html
<!DOCTYPE html>
<html lang="en">
<head>
<meta charset="utf-8">
<title>The Paper Lantern Ledger — Book Cover</title>
<link rel="stylesheet" href="https://fonts.googleapis.com/css2?family=Archivo+Black&family=Special+Elite&family=Permanent+Marker&display=swap">
<style>
  :root {
    --paper: #ffffff;
    --ink: #000000;
    --blood: #8b1111;
  }
  html, body {
    margin: 0;
    padding: 0;
    width: 800px;
    height: 1200px;
    overflow: hidden;
    background: var(--paper);
  }
  .cover {
    display: block;
    width: 800px;
    height: 1200px;
  }
  .label-strip { fill: var(--ink); }
  .label-text {
    font-family: "Special Elite", monospace;
    font-size: 17px;
    fill: var(--paper);
    letter-spacing: 4px;
  }
  .redaction-bar { fill: var(--ink); }
  .title-block {
    font-family: "Archivo Black", sans-serif;
    fill: var(--ink);
  }
  .title-accent {
    font-family: "Permanent Marker", cursive;
    fill: var(--blood);
  }
</style>
</head>
<body>
<svg class="cover" viewBox="0 0 800 1200" xmlns="http://www.w3.org/2000/svg" role="img" aria-label="The Paper Lantern Ledger, by Peter Hoskins and Tamsin Ogilvy, foreword by Marla Quentin">
  <!-- foreword credit -->
  <g class="foreword">
    <polygon class="label-strip" points="192,77 608,71 608,102 192,108"/>
    <text class="label-text" x="400" y="97" text-anchor="middle" transform="rotate(-0.8 400 90)" textLength="396" lengthAdjust="spacing">FOREWORD BY MARLA QUENTIN</text>
  </g>

  <!-- title -->
  <g class="title">
    <text class="title-accent" x="101" y="533" font-size="62" textLength="120" lengthAdjust="spacingAndGlyphs">THE</text>

    <polygon class="redaction-bar" points="80,541 270,542 269,609 80,608"/>
    <text class="title-block" x="279" y="603" font-size="85" textLength="324" lengthAdjust="spacingAndGlyphs">PAPER</text>

    <text class="title-block" x="83" y="675" font-size="89" textLength="638" lengthAdjust="spacingAndGlyphs">LANTERN</text>

    <polygon class="redaction-bar" points="80,692 231,691 231,750 80,751"/>
    <polygon class="redaction-bar" points="242,686 656,680 657,748 243,753"/>

    <text class="title-accent" x="520" y="824" font-size="66" textLength="170" lengthAdjust="spacingAndGlyphs">LEDGER</text>
  </g>

  <!-- authors -->
  <g class="authors">
    <rect class="label-strip" x="175" y="1038" width="241" height="40"/>
    <text class="label-text" x="184" y="1064" textLength="222" lengthAdjust="spacing">PETER HOSKINS &amp;</text>
    <rect class="label-strip" x="358" y="1081" width="224" height="40"/>
    <text class="label-text" x="376" y="1107" textLength="198" lengthAdjust="spacing">TAMSIN OGILVY</text>
  </g>
</svg>
</body>
</html>
```